Talk Show Flyer Design

Please read for exactly what I need the flyer to say.

Lorna Pike is the person with black jacket
Tereza has the red dress
Owen Marsh has the gray suit on.

Please read below and see attached images:

Coming Soon!

Painters & Poets Hour

With
Lorna Pike
Tereza Volkov
&
Owen Marsh

Add Wavelink logo

*Recorded For Television*
(30 MILLION TV HOUSEHOLDS)

Live Social Media Airing:
5 Million Followers/Audience

```html
<!DOCTYPE html>
<html lang="en">
<head>
<meta charset="utf-8">
<title>Painters &amp; Poets Hour – Coming Soon</title>
<link rel="stylesheet" href="https://fonts.googleapis.com/css2?family=Baloo+2:wght@800&family=Cormorant+Garamond:wght@600&family=Open+Sans:wght@700&family=PT+Sans+Narrow:wght@700&display=swap">
<style>
  :root {
    --red: #e3141b;
    --red-bright: #f0232a;
    --red-deep: #a80c10;
    --flame: #f26a1f;
    --ink: #111111;
    --white: #ffffff;
    --cream: #fbe6e7;
    --outline: #b3151b;
    --mic-disc: #3b1d1c;
  }
  * { margin: 0; padding: 0; box-sizing: border-box; }
  html, body { width: 848px; height: 1200px; overflow: hidden; }
  body { font-family: "Open Sans", Arial, sans-serif; }

  .flyer {
    position: relative;
    width: 848px;
    height: 1200px;
    overflow: hidden;
    background: var(--red);
  }
  .flyer__backdrop {
    position: absolute; inset: 0;
    background:
      radial-gradient(ellipse at 8% 30%, rgba(242,106,31,.55), transparent 45%),
      radial-gradient(ellipse at 95% 75%, rgba(242,106,31,.5), transparent 40%),
      radial-gradient(ellipse at 10% 90%, rgba(242,106,31,.5), transparent 40%),
      linear-gradient(180deg, var(--red-bright), var(--red) 60%, var(--red-deep));
  }
  .feature-band {
    position: absolute; left: 0; top: 432px; width: 848px; height: 430px;
    background: rgba(255, 60, 60, .35);
  }

  .headline {
    position: absolute;
    font-family: "Baloo 2", "Arial Rounded MT Bold", sans-serif;
    font-weight: 800;
    color: var(--cream);
    -webkit-text-stroke: 6px var(--outline);
    paint-order: stroke fill;
    text-shadow: 4px 5px 0 var(--red-deep);
    line-height: 1;
    transform: rotate(-7deg);
    transform-origin: left center;
  }
  .headline--coming { left: 26px; top: 66px; font-size: 148px; letter-spacing: -2px; }
  .headline--soon { left: 318px; top: 160px; font-size: 148px; letter-spacing: -2px; }

  .station-badge {
    position: absolute; left: 628px; top: -5px;
    width: 198px; height: 198px; border-radius: 50%;
    background: var(--white);
    display: flex; align-items: center; justify-content: center;
  }
  .station-badge__name {
    font-family: "Open Sans", Arial, sans-serif;
    font-weight: 700; font-size: 30px; color: var(--red);
  }

  .mic-disc {
    position: absolute; left: 590px; top: 196px;
    width: 330px; height: 330px; border-radius: 50%;
    background: var(--mic-disc);
  }
  .mic-disc__art {
    position: absolute; left: 100px; top: 70px; width: 150px; height: 150px;
    border-radius: 40% 40% 30% 30%;
    background: radial-gradient(circle at 40% 40%, #e2302a, #7a1311 75%);
    transform: rotate(-35deg);
  }

  .show-title {
    position: absolute; left: 24px; top: 376px;
    height: 43px;
    border: 2px solid var(--white);
    font-family: "Cormorant Garamond", "Times New Roman", serif;
    font-weight: 600; font-size: 44px; line-height: 37px;
    letter-spacing: 2px;
    color: var(--red);
    -webkit-text-stroke: 1.2px var(--white);
    padding: 0 4px 0 6px; white-space: nowrap;
  }

  .swan-art {
    position: absolute; left: 104px; top: 444px; width: 462px; height: 416px;
    border-radius: 46% 30% 48% 52% / 40% 30% 60% 60%;
    background: linear-gradient(160deg, rgba(255,255,255,.95), rgba(255,238,238,.92));
  }

  .guest-photo { position: absolute; }
  .guest-photo--tereza {
    left: 203px; top: 506px; width: 316px; height: 198px;
    background: linear-gradient(180deg, #e9c39e 0%, #d8a47f 45%, #d3161d 70%, #b50f14 100%);
  }
  .guest-photo--round { width: 198px; height: 198px; border-radius: 50%; }
  .guest-photo--owen {
    left: 122px; top: 626px;
    background: linear-gradient(180deg, #f4f4f4 0%, #cfcfd2 55%, #a9a9ad 100%);
  }
  .guest-photo--lorna {
    left: 465px; top: 590px;
    background: linear-gradient(180deg, #e6dcd2 0%, #9b7b62 40%, #1d1a1a 75%);
  }

  .guest-name {
    position: absolute;
    font-family: "PT Sans Narrow", "Arial Narrow", sans-serif;
    font-weight: 700; color: var(--white); white-space: nowrap; line-height: 1;
    text-shadow: 2px 2px 3px rgba(0,0,0,.45);
  }
  .guest-name--tereza { left: 221px; top: 460px; font-size: 42px; }
  .guest-name--lorna { left: 592px; top: 548px; font-size: 46px; }
  .guest-name--owen { left: 20px; top: 818px; font-size: 44px; }

  .details {
    position: absolute; left: 0; width: 848px; text-align: center; white-space: nowrap; line-height: 1;
    font-family: "Open Sans", Arial, sans-serif; font-weight: 700;
  }
  .details--broadcast { top: 876px; font-size: 50px; color: var(--ink); letter-spacing: -0.5px; }
  .details--households { top: 942px; font-size: 37px; color: var(--white); letter-spacing: -0.5px; }
  .details--live { top: 1054px; font-size: 42px; color: var(--white); }
  .details--audience { top: 1112px; font-size: 44px; color: var(--ink); }

  .divider {
    position: absolute; left: 89px; top: 1030px; width: 692px; height: 3px;
    background: var(--white);
  }
</style>
</head>
<body>
<main class="flyer">
  <div class="flyer__backdrop" role="img" aria-label="Red and orange flame pattern background"></div>
  <div class="feature-band"></div>

  <h1>
    <span class="headline headline--coming">Coming</span>
    <span class="headline headline--soon">Soon</span>
  </h1>

  <div class="station-badge"><span class="station-badge__name">Larkmoor</span></div>

  <div class="mic-disc">
    <div class="mic-disc__art" role="img" aria-label="Red vintage studio microphone"></div>
  </div>

  <p class="show-title">Painters &amp; Poets Hour with</p>

  <div class="swan-art" role="img" aria-label="White swan silhouette"></div>

  <div class="guest-photo guest-photo--tereza" role="img" aria-label="Tereza Volkov in a red dress holding a crown"></div>
  <div class="guest-photo guest-photo--round guest-photo--owen" role="img" aria-label="Owen Marsh in a gray suit"></div>
  <div class="guest-photo guest-photo--round guest-photo--lorna" role="img" aria-label="Lorna Pike in a black jacket"></div>

  <p class="guest-name guest-name--tereza">Tereza Volkov</p>
  <p class="guest-name guest-name--lorna">Lorna Pike</p>
  <p class="guest-name guest-name--owen">Owen Marsh</p>

  <p class="details details--broadcast">Recorded For Television</p>
  <p class="details details--households">(30 MILLION TV HOUSEHOLDS)</p>
  <div class="divider"></div>
  <p class="details details--live">Live Social Media Airing:</p>
  <p class="details details--audience">5 Million Followers/Audience</p>
</main>
</body>
</html>
```